Professional Reserve Fund Planners require print ad

The Accredited Capital Outlay Forecasting (ACF) designation is the only designated professional that has specific education in the preparation of reserve fund studies.
Reserve Fund Studies are mandatory for Condominiums across Canada and we want to promote our designation as a step above others performing studies and should be sought out by clients if they would like to have the best studies.
The advertising will require space for the Habitat Stewards Guild Council (HSGC) logo and the contact information for planners who have the accreditation.
Some points to consider: The designation has been in place since 1999. Specific training in the preparation of long term reserve fund studies with a specific focus on financial fundamentals, technical proficiency, investing reserves appropriately and legislation.
This will be a full page magazine ad for a trade publication called Strata Ledger by PressVane. Thanks.
Please note that the ads i have uploaded are simply ads that I feel capture the essence of what I am trying to achieve. I believe the ads I have uploaded are indicating a feeling of trust in the designation THEY are promoting. I want our designation ad to feel the same. You are out looking for someone to perform a reserve fund study. You can find the same old schmuck or you can find someone who has invested time and money seeking a better education and the designation ACF shows dedication, ethical standards and educational level that should give clients the feeling they are getting the best of the best.
For property managers and a Board of Directors, a properly prepared and timely reserve fund study will keep the Board of Directors and/or owners off their back. I always use the concept of "hiring us makes your job easier" and words or phrases like value-add partner, service provider, collaboration, reasonable, achievable.
Condominium owners looking for professional reserve fund study services.
Condominium Board of Directors
Condominium Property Managers
Advertising

```html
<!DOCTYPE html>
<html lang="en">
<head>
<meta charset="utf-8">
<title>Accredited Capital Outlay Forecasting (ACF) – Print Ad</title>
<link rel="stylesheet" href="https://fonts.googleapis.com/css2?family=Open+Sans:wght@400;600;700&family=Oswald:wght@600&display=swap">
<style>
  :root {
    --red: #e8231f;
    --red-deep: #d81d1a;
    --ink: #111111;
    --paper: #f1f1f1;
    --card: #f7f7f7;
    --card-edge: #d4d4d4;
    --muted: #9aa9b3;
    --white: #ffffff;
  }
  * { margin: 0; padding: 0; box-sizing: border-box; }
  html, body { width: 824px; height: 1200px; overflow: hidden; background: var(--white); }
  .ad {
    position: relative; width: 824px; height: 1200px; overflow: hidden;
    background: var(--paper);
    font-family: "Open Sans", Arial, sans-serif; color: var(--ink);
  }
  .top-band { position: absolute; left: 0; top: 0; width: 100%; height: 22px; background: var(--red); }

  .brand { position: absolute; left: 34px; top: 39px; display: flex; align-items: center; gap: 10px; }
  .brand-square { width: 83px; height: 80px; background: var(--red); }
  .brand-name { font-weight: 700; font-size: 15.5px; line-height: 22px; color: var(--ink); margin-top: 34px; }

  .hero {
    position: absolute; left: 0; top: 138px; width: 824px; height: 520px;
    background: linear-gradient(100deg, #2b2f3a 0%, #6c6a72 22%, #e9dcd4 45%, #f3ece8 60%, #cfd9e6 80%, #e6ebf2 100%);
  }
  .hero::after {
    content: ""; position: absolute; left: 0; bottom: 0; width: 100%; height: 150px;
    background: linear-gradient(180deg, rgba(205,160,110,0) 0%, #c89b68 55%, #b98a58 100%);
  }
  .since {
    position: absolute; left: 457px; top: 452px; width: 367px; height: 118px;
    background: rgba(232, 60, 55, 0.72); color: var(--white); padding: 18px 0 0 40px; z-index: 2;
  }
  .since-lead { font-size: 24px; font-weight: 600; letter-spacing: 0.3px; line-height: 30px; }
  .since-year { font-size: 37px; font-weight: 700; line-height: 44px; }

  .title-bar {
    position: absolute; left: 43px; top: 679px; width: 743px; height: 76px;
    background: var(--red); box-shadow: 3px 4px 4px rgba(0,0,0,0.25);
    display: flex; align-items: center; justify-content: center;
    font-family: "Oswald", "Arial Narrow", sans-serif; font-weight: 600;
    font-size: 33px; color: var(--white); letter-spacing: 0.3px;
  }
  .subtitle {
    position: absolute; left: 43px; top: 776px; font-size: 20px; font-weight: 600; letter-spacing: 0.1px;
  }

  .topics { position: absolute; left: 45px; top: 819px; display: flex; gap: 11px; }
  .topic {
    position: relative; width: 139px; height: 118px; background: var(--card);
    border: 1px solid var(--card-edge); box-shadow: 2px 3px 4px rgba(0,0,0,0.15);
    display: flex; align-items: center; justify-content: center; text-align: center;
    font-size: 16.5px; font-weight: 600; line-height: 27px; text-transform: uppercase;
  }
  .topic .clip { position: absolute; left: 8px; top: -12px; width: 12px; height: 26px; }

  .prompt {
    position: absolute; left: 93px; top: 983px; font-size: 29px; line-height: 44px; letter-spacing: 0.6px;
  }
  .divider { position: absolute; left: 468px; top: 972px; height: 140px; border-left: 2px dotted #555; }
  .contact { position: absolute; left: 493px; top: 975px; }
  .contact-title { font-size: 19.5px; font-weight: 600; line-height: 28px; }
  .contact-field { margin-top: 10px; font-size: 19.5px; color: var(--muted); display: flex; align-items: baseline; gap: 8px; }
  .contact-field:first-of-type { margin-top: 14px; }
  .contact-field .line { border-bottom: 2px dotted var(--muted); width: 205px; height: 1px; }

  .footer-band {
    position: absolute; left: 0; top: 1144px; width: 100%; height: 56px; background: var(--red-deep);
    display: flex; align-items: center; justify-content: center;
    color: var(--white); font-size: 33px; letter-spacing: 0.8px;
  }
</style>
</head>
<body>
<main class="ad">
  <div class="top-band"></div>

  <header class="brand">
    <div class="brand-square"></div>
    <div class="brand-name">The Habitat Stewards Guild Council<br>Conseil de la guilde des intendants de l'habitat</div>
  </header>

  <div class="hero" role="img" aria-label="Photo of a smiling advisor in a suit reviewing a laptop with a senior couple at a wooden desk"></div>

  <div class="since">
    <div class="since-lead">SHARING KNOWLEDGE</div>
    <div class="since-year">SINCE 1999</div>
  </div>

  <h1 class="title-bar">THE ACCREDITED CAPITAL OUTLAY FORECASTING (ACF)</h1>
  <p class="subtitle">SPECIALISED TRAINING EXPERTISING YOU ON RESERVE FUND STUDIES</p>

  <ul class="topics">
    <li class="topic"><svg class="clip" viewBox="0 0 12 26"><path d="M3 8V4a3 3 0 0 1 6 0v16a2 2 0 0 1-4 0V8" fill="none" stroke="#8a8a8a" stroke-width="1.5"/></svg>Financial<br>Fundamentals</li>
    <li class="topic"><svg class="clip" viewBox="0 0 12 26"><path d="M3 8V4a3 3 0 0 1 6 0v16a2 2 0 0 1-4 0V8" fill="none" stroke="#8a8a8a" stroke-width="1.5"/></svg>Technical<br>Proficiency</li>
    <li class="topic"><svg class="clip" viewBox="0 0 12 26"><path d="M3 8V4a3 3 0 0 1 6 0v16a2 2 0 0 1-4 0V8" fill="none" stroke="#8a8a8a" stroke-width="1.5"/></svg>Reserves<br>Optimization</li>
    <li class="topic"><svg class="clip" viewBox="0 0 12 26"><path d="M3 8V4a3 3 0 0 1 6 0v16a2 2 0 0 1-4 0V8" fill="none" stroke="#8a8a8a" stroke-width="1.5"/></svg>Applying<br>Legislation</li>
    <li class="topic"><svg class="clip" viewBox="0 0 12 26"><path d="M3 8V4a3 3 0 0 1 6 0v16a2 2 0 0 1-4 0V8" fill="none" stroke="#8a8a8a" stroke-width="1.5"/></svg>Fund<br>Management</li>
  </ul>

  <p class="prompt">Are you looking for<br>someone to perform<br>a reserve fund study.</p>

  <div class="divider"></div>

  <section class="contact">
    <h2 class="contact-title">CONTACT INFORMATION OF<br>ACCREDITATED PLANNER</h2>
    <div class="contact-field">NAME <span class="line"></span></div>
    <div class="contact-field">PHONE <span class="line"></span></div>
  </section>

  <footer class="footer-band">www.hsgc.ca/en/designations-acf</footer>
</main>
</body>
</html>
```